Web Site Design

We need to design the whole web site for our small start up. We sell hospitality and culinary art internships abroad. I did my own design with WIX which is horrible meanwhile I started with my business. You can see it www.brindle-passage.org I will need you to create a new and attractive web site and to leave it working on wix. The internship destinations are United Arab Emirates, Thailand, China, Spain, Brazil and maybe leave a couple of pages for future destinations.You could also get other ideas of other sites that do internships.

Target Market(s)

Students and recent graduates of hospitality and culinary art majors

Industry/Entity Type

Education

Number of Pages Required

5+ page

Requirements
Must have
• Addittional to our program destinations, or to the pages in the current site. The website must contain a page for Universities or Hotels who require our service

```html
<!DOCTYPE html>
<html lang="en">
<head>
<meta charset="utf-8">
<title>Brindle Passage – Hospitality Internship Program</title>
<link rel="stylesheet" href="https://fonts.googleapis.com/css2?family=Tinos:ital,wght@0,400;0,700;1,400&display=swap">
<style>
:root{
  --teal:#2b8785;
  --teal-dark:#1f6b69;
  --ink:#222;
  --muted:#666;
  --light:#f2f2f2;
  --line:#d6d6d6;
  --dark:#1c1c1c;
  --white:#fff;
}
*{box-sizing:border-box;margin:0;padding:0}
html,body{width:1200px;height:4299px;overflow:hidden}
body{font-family:"Tinos",serif;color:var(--ink);background:var(--white);position:relative}
section,header,footer{position:absolute;left:0;width:1200px;overflow:hidden}
.btn{display:inline-block;background:var(--teal);color:var(--white);font-weight:700;font-size:15px;padding:13px 26px;letter-spacing:.5px}
.btn-outline{display:inline-block;border:1px solid var(--line);background:var(--white);font-size:13px;font-weight:700;letter-spacing:1.5px;padding:10px 36px}
.section-title{position:relative;text-align:center;font-size:34px;font-weight:700;letter-spacing:3px}
.placeholder{position:absolute}

/* hero */
.hero{top:0;height:609px}
.hero-photo{inset:0;background:linear-gradient(120deg,#9a8f86 0%,#d8d2cc 35%,#efe9e2 55%,#a39483 80%,#5c4c3e 100%)}
.hero-shade{position:absolute;inset:0;background:linear-gradient(180deg,rgba(0,0,0,.15),rgba(0,0,0,.35))}
.nav{position:absolute;top:0;left:0;right:0;height:40px;background:rgba(20,20,20,.45);display:flex;justify-content:center;align-items:flex-start}
.nav ul{display:flex;list-style:none;gap:30px;color:var(--white);font-size:15px;font-weight:700;height:40px;align-items:center}
.brand{width:150px;height:88px;margin:0 40px;background:rgba(20,20,20,.75);display:flex;flex-direction:column;align-items:center;justify-content:center;color:var(--white);font-size:13px;font-weight:700;letter-spacing:1px;gap:6px}
.brand-dot{width:26px;height:26px;border:2px solid var(--white);border-radius:50%}
.hero-copy{position:absolute;top:370px;left:0;right:0;text-align:center;color:var(--white)}
.hero-copy h1{font-size:44px;font-weight:700;letter-spacing:1px}
.hero-copy p{font-size:24px;font-weight:700;margin-top:8px}
.hero-copy .btn{margin-top:30px}
.dots{position:absolute;top:588px;left:0;right:0;display:flex;justify-content:center;gap:8px}
.dots i{width:9px;height:9px;border-radius:50%;background:rgba(255,255,255,.6)}
.dots i:first-child{background:var(--white)}

/* intro */
.intro{top:609px;height:405px}
.intro-text{position:absolute;left:172px;top:70px;width:400px;font-size:30px;line-height:1.3}
.intro .btn{position:absolute;left:172px;top:270px}
.intro-photo{left:609px;top:70px;width:420px;height:258px;background:linear-gradient(180deg,#8cc4ea 0%,#cfe6f4 45%,#e9e4dc 60%,#3bb7d2 80%,#2a97bc 100%)}

/* benefits */
.benefits{top:1014px;height:544px;background:var(--light)}
.benefits-photo{left:0;top:0;width:602px;height:544px;background:linear-gradient(135deg,#5b5450 0%,#a9a099 40%,#e3dfdb 55%,#6f655e 100%)}
.play{position:absolute;left:270px;top:252px;width:62px;height:42px;background:#e62117;border-radius:10px}
.play::after{content:"";position:absolute;left:25px;top:12px;border-left:16px solid var(--white);border-top:9px solid transparent;border-bottom:9px solid transparent}
.benefits-list{position:absolute;left:660px;top:40px;width:500px}
.benefits-list h2{font-size:34px;letter-spacing:3px;color:#444;padding-bottom:14px;border-bottom:1px solid var(--line);margin-bottom:26px}
.benefit{display:flex;gap:16px;margin-bottom:22px}
.benefit svg{flex:none;width:28px;height:28px;fill:var(--teal)}
.benefit h3{font-size:16px;letter-spacing:1px}
.benefit p{font-size:14px;color:var(--muted);margin-top:3px;line-height:1.35}

/* destinations */
.destinations{top:1558px;height:555px;background:#f4f4f4}
.destinations .section-title{margin-top:70px}
.dest-cards{position:absolute;top:168px;left:150px;display:flex;gap:43px}
.dest{width:273px;text-align:center}
.dest-photo{position:relative;height:251px;border:6px solid var(--white);box-shadow:0 2px 6px rgba(0,0,0,.15)}
.dest-photo span{position:absolute;left:40px;right:40px;top:105px;background:rgba(20,20,20,.7);color:var(--white);font-size:14px;font-weight:700;padding:8px 0}
.uae{background:linear-gradient(180deg,#6fb3e4,#c7e2f1 60%,#2d7fa8)}
.thai{background:linear-gradient(180deg,#e9a26c,#f6d7b8 55%,#3c8fa4)}
.spain{background:linear-gradient(180deg,#3d83c4,#9fc7e5 55%,#7a5d46)}
.dest .btn-outline{margin-top:38px}
.arrow-box{position:absolute;top:180px;width:42px;height:42px;background:var(--teal);display:flex;align-items:center;justify-content:center}
.arrow-box svg{width:16px;height:16px;stroke:var(--white);fill:none;stroke-width:3}

/* process */
.process{top:2113px;height:513px;background:#fafafa}
.process .section-title{margin-top:76px}
.process .kicker{text-align:center;font-size:12px;letter-spacing:3px;color:var(--muted);margin-top:4px}
.steps{position:absolute;top:226px;left:110px;width:980px;display:grid;grid-template-columns:repeat(4,1fr);gap:30px;text-align:center}
.step svg{width:52px;height:52px;stroke:var(--ink);fill:none;stroke-width:2}
.step h3{font-size:15px;letter-spacing:1px;margin-top:6px}
.step p{font-size:12px;color:var(--muted);line-height:1.45;margin-top:6px}
.step-nav{position:absolute;top:446px;left:0;right:0;display:flex;justify-content:center;gap:14px}
.step-nav svg{width:20px;height:24px;stroke:#444;fill:none;stroke-width:2}

/* employ */
.employ{top:2626px;height:426px}
.employ-photo{inset:0;background:linear-gradient(90deg,#4a3b32 0%,#a79485 30%,#d9cfc5 55%,#6b5647 80%,#2b2420 100%)}
.employ-box{position:absolute;left:322px;top:78px;width:573px;height:269px;background:rgba(255,255,255,.78);text-align:center;padding-top:26px}
.employ-box h2{font-size:42px;letter-spacing:3px}
.employ-box .kicker{font-size:12px;letter-spacing:3px;color:#555}
.employ-box h3{font-size:24px;letter-spacing:1px;margin-top:18px;font-weight:400}
.employ-box p{font-size:15px;color:#444}
.employ-box .btn{margin-top:22px}

/* partners */
.partners{top:3052px;height:261px}
.partners .section-title{margin-top:62px;font-size:30px}
.partner-row{position:absolute;top:176px;left:50px;right:50px;display:flex;justify-content:space-between;align-items:center}
.partner{display:flex;align-items:center;gap:7px;font-size:15px;font-weight:700;color:#333}
.partner i{width:12px;height:12px;border-radius:50%;background:#333}

/* enrollment */
.enroll{top:3313px;height:491px;background:#f6f6f6}
.enroll-backdrop{inset:0;background:linear-gradient(180deg,#f1eeec 0%,#f8f8f8 40%,#f8f8f8 70%,#eef0ea 100%)}
.enroll .section-title{margin-top:106px}
.enroll form{position:absolute;left:172px;top:176px;width:856px}
.fields{display:grid;grid-template-columns:repeat(4,1fr);gap:20px}
.field{height:42px;border:1px solid var(--line);background:var(--white);font-size:13px;color:#888;padding:12px 12px;display:flex;justify-content:space-between}
.message{height:122px;margin-top:12px}
.enroll .btn{display:block;width:170px;margin:32px auto 0;text-align:center}

/* offices */
.offices{top:3804px;height:423px;background:var(--dark);color:var(--white);text-align:center}
.offices .section-title{margin-top:76px;font-size:30px}
.office-row{position:absolute;top:178px;left:180px;right:180px;display:grid;grid-template-columns:repeat(4,1fr)}
.office .flag{width:54px;height:54px;border-radius:50%;margin:0 auto 10px}
.office h3{font-size:15px;letter-spacing:1px}
.office p{font-size:14px;margin-top:4px}
.mx{background:linear-gradient(90deg,#1a7a3f 33%,#fff 33% 66%,#c8332f 66%)}
.us{background:repeating-linear-gradient(180deg,#b8283a 0 6px,#fff 6px 12px)}
.eu{background:#1f4aa8}
.au{background:#1a2f78}
.offices .email{position:absolute;top:326px;left:0;right:0;font-size:16px;font-weight:700}
.social{position:absolute;top:362px;left:0;right:0;display:flex;justify-content:center;gap:12px}
.social i{width:14px;height:14px;border-radius:50%;background:#888}
footer{top:4227px;height:72px;background:#111;color:#777;font-size:13px;text-align:center;line-height:72px}
</style>
</head>
<body>

<header class="hero">
  <div class="placeholder hero-photo" role="img" aria-label="Chefs in white toques plating food in a professional kitchen"></div>
  <div class="hero-shade"></div>
  <nav class="nav">
    <ul><li>Home</li><li>About us</li><li>Destinations</li><li>Process</li></ul>
    <div class="brand"><span class="brand-dot"></span>BRINDLE PASSAGE</div>
    <ul><li>Placement</li><li>Need Us</li><li>Contact</li><li>Contact</li></ul>
  </nav>
  <div class="hero-copy">
    <h1>Hospitality Internship Program</h1>
    <p>Culinary - F &amp; B - Front Office - Guest Relations</p>
    <span class="btn">Apply Now</span>
  </div>
  <div class="dots"><i></i><i></i><i></i></div>
</header>

<section class="intro">
  <p class="intro-text">Hospitality internships are our specialty! Take your paid internship in one of our top international five-star hotels</p>
  <span class="btn">View Our Process</span>
  <div class="placeholder intro-photo" role="img" aria-label="Resort hotel with a large outdoor swimming pool"></div>
</section>

<section class="benefits">
  <div class="placeholder benefits-photo" role="img" aria-label="Video still of a chef cooking before an audience"><span class="play"></span></div>
  <div class="benefits-list">
    <h2>BENEFITS</h2>
    <div class="benefit"><svg viewBox="0 0 24 24"><path d="M3 20l7-12 4 6 3-4 4 10z"/></svg><div><h3>QUALITY</h3><p>Work and train at the best hotels</p></div></div>
    <div class="benefit"><svg viewBox="0 0 24 24"><path d="M4 18l6-6 4 4 6-8v4h2V4h-6v2h3l-5 7-4-4-7 7z"/></svg><div><h3>AFFORDABILITY</h3><p>Payment after placement</p></div></div>
    <div class="benefit"><svg viewBox="0 0 24 24"><path d="M2 14l20-8-6 14-4-5z"/></svg><div><h3>INTERNATIONAL</h3><p>Work and live in the best cities<br>United Arab Emirates, Thailand, China, Spain, Brazil.</p></div></div>
    <div class="benefit"><svg viewBox="0 0 24 24"><path d="M4 3h12l4 4v14H4z"/></svg><div><h3>PROFESSIONALISM</h3><p>Improve your resume and your professional future</p></div></div>
    <div class="benefit"><svg viewBox="0 0 24 24"><path d="M3 7h18v12H3zM8 7V4h8v3"/></svg><div><h3>INTERNSHIPS</h3><p>Only international internships and well established career programs</p></div></div>
  </div>
</section>

<section class="destinations">
  <h2 class="section-title">DESTINATIONS</h2>
  <div class="arrow-box" style="left:0"><svg viewBox="0 0 16 16"><path d="M11 2L5 8l6 6"/></svg></div>
  <div class="arrow-box" style="right:0"><svg viewBox="0 0 16 16"><path d="M5 2l6 6-6 6"/></svg></div>
  <div class="dest-cards">
    <div class="dest"><div class="dest-photo uae" role="img" aria-label="City skyline and coast in the United Arab Emirates"><span>United Arab Emirates</span></div><span class="btn-outline">APPLY NOW</span></div>
    <div class="dest"><div class="dest-photo thai" role="img" aria-label="Beach resort in Thailand at sunset"><span>Thailand</span></div><span class="btn-outline">APPLY NOW</span></div>
    <div class="dest"><div class="dest-photo spain" role="img" aria-label="Hotel terrace in Spain"><span>Spain</span></div><span class="btn-outline">APPLY NOW</span></div>
  </div>
</section>

<section class="process">
  <h2 class="section-title">OUR PROCESS</h2>
  <p class="kicker">READY TO GO?</p>
  <div class="steps">
    <div class="step"><svg viewBox="0 0 52 52"><rect x="12" y="8" width="28" height="36"/><path d="M18 18h16M18 26h16M18 34h10"/></svg><h3>APPLY</h3><p>Send your CV for pre-screening and tell us where you want to train.</p></div>
    <div class="step"><svg viewBox="0 0 52 52"><rect x="8" y="14" width="36" height="26"/><path d="M8 22h36M30 32h8"/></svg><h3>DEPOSIT</h3><p>If you are preselected for the program we confirm your place with a deposit to secure your spot.</p></div>
    <div class="step"><svg viewBox="0 0 52 52"><circle cx="20" cy="18" r="7"/><circle cx="34" cy="18" r="7"/><path d="M8 42c2-10 22-10 24 0M22 42c2-10 22-10 24 0"/></svg><h3>INTERVIEW</h3><p>We will match you with three companies that fit your track and schedule an interview.</p></div>
    <div class="step"><svg viewBox="0 0 52 52"><rect x="10" y="10" width="32" height="34"/><path d="M16 18h20M16 26h20M16 34h12"/></svg><h3>PLACEMENT</h3><p>Acceptance of internship offer. Invitation letter issued.</p></div>
  </div>
  <div class="step-nav"><svg viewBox="0 0 20 24"><path d="M14 3L5 12l9 9"/></svg><svg viewBox="0 0 20 24"><path d="M6 3l9 9-9 9"/></svg></div>
</section>

<section class="employ">
  <div class="placeholder employ-photo" role="img" aria-label="Chef plating dishes and a waiter in uniform holding a napkin"></div>
  <div class="employ-box">
    <h2>EMPLOY THE BEST</h2>
    <p class="kicker">LET US ASSIST YOU TO FIND INTERNS</p>
    <h3>HOSPITALITY INTERNSHIP PROGRAM</h3>
    <p>Culinary, F&amp;B, Front Office, Guest Relations Training</p>
    <span class="btn">ENQUIRE NOW</span>
  </div>
</section>

<section class="partners">
  <h2 class="section-title">PREVIOUS INTERNS HAVE SECURED POSITIONS AT</h2>
  <div class="partner-row">
    <span class="partner"><i></i>Harbor Crest</span>
    <span class="partner"><i></i>Maren Hall</span>
    <span class="partner"><i></i>St. Alder</span>
    <span class="partner"><i></i>Shorewood</span>
    <span class="partner"><i></i>Orchid Row</span>
    <span class="partner"><i></i>Westmere</span>
    <span class="partner"><i></i>Holloway Inn</span>
    <span class="partner"><i></i>Kestrel Palace</span>
  </div>
</section>

<section class="enroll">
  <div class="placeholder enroll-backdrop" role="img" aria-label="Light kitchen backdrop with fresh tomatoes and herbs at the edges"></div>
  <h2 class="section-title">OUR FORM FOR ENROLLMENT</h2>
  <form>
    <div class="fields">
      <div class="field">Name</div>
      <div class="field">Email Address</div>
      <div class="field">Phone Number</div>
      <div class="field">Intern Destination <span>▾</span></div>
    </div>
    <div class="field message">Message</div>
    <span class="btn">ENROLL NOW</span>
  </form>
</section>

<section class="offices">
  <h2 class="section-title">OUR OFFICES</h2>
  <div class="office-row">
    <div class="office"><div class="flag mx"></div><h3>MEXICO</h3><p>+52 55 0100 4471</p></div>
    <div class="office"><div class="flag us"></div><h3>UNITED STATES</h3><p>+1 555-010-2938</p></div>
    <div class="office"><div class="flag eu"></div><h3>EUROPE</h3><p>+33 7 0100 2846</p></div>
    <div class="office"><div class="flag au"></div><h3>AUSTRALIA</h3><p>+61 400 010 572</p></div>
  </div>
  <p class="email">Email us: info@brindle-passage.org</p>
  <div class="social"><i></i><i></i><i></i><i></i><i></i></div>
</section>

<footer>© Copyright Brindle Passage 2014</footer>

</body>
</html>
```